Family history tech product tailored for moms needs banner ads

plume.com is launching next week and we've partnered with an ad group that will be launching a campaign on school district websites that will be pushed to 250k moms of school age children.

We're launching a $199 product that shows you more about who you are through your family's history. We connect people wanting to learn more about themselves with expert researcher/genealogist who will uncover their past and find the stories of their ancestors.

See branding guidelines below as well as the landing page we're designing where these ads will take you.

Here is the landing page design:
https://chatbox-files.example/X839KQ2M1-G72P4TTR8-kf4e1mzq90

Target Market(s)

Mom's of kids in elementary and middle school.

Persona:
Mom, 38 years old, 2 kids (age 6 and 8)
Lives in Dallas, drives a 2016 Vormak Ridgel
She and husband met in college. She was a nurse, but she stopped working to be a full-time mom
Husband is in financial consulting, household income of $140,000
When kids at school, she runs errands, works out, meets up with girlfriends for coffee
She shops at Sorvanta, has active hobbies
She is always busy, there’s not enough time for her family; she is worried that her kids may become distant because of how busy the family is
She values time with family most, soccer weekends, financial stability, college for the kids
Wants to connect more with the kids and the family to increase the bond, and she thinking having more context for the family will help them bond around a common history
Her objections to Plume are lack of trust in a new service, time it will cost her to get the info she wants to achieve her goals

Industry/Entity Type

Startup

Font styles to use
Other font styles liked:
• follow style guide

Requirements
Must have
• Must follow the design pattern in our branding guide.
• https://www.filecrate.example/s/kqm4tnw819zpxa/Screenshot%202016-11-30%2013.39.48.png?dl=0
Nice to have
• Good copy, I'm less worried about that though. We can work together on that.
Should not have
• Stock imagery that sucks. I'm really opposed to anything that looks like it is from the 2001 - 2011

```html
<!DOCTYPE html>
<html lang="en">
<head>
<meta charset="utf-8">
<title>Plume — Banner Set</title>
<link rel="stylesheet" href="https://fonts.googleapis.com/css2?family=PT+Sans:wght@400;700&family=PT+Sans+Narrow:wght@400;700&display=swap">
<style>
  :root {
    --page-bg: #e8e9eb;
    --brand-deep: #0a6dc2;
    --brand-sky: #3aa2f1;
    --cta-teal: #1fbdca;
    --paper: #ffffff;
    --photo-light: #e9d9cf;
    --photo-mid: #8c7564;
    --photo-blue: #3c8fd6;
  }
  * { box-sizing: border-box; margin: 0; padding: 0; }
  html, body { width: 1200px; height: 1200px; overflow: hidden; }
  body {
    background: var(--page-bg);
    position: relative;
    font-family: "PT Sans", Arial, sans-serif;
    color: var(--paper);
  }
  .banner {
    position: absolute;
    background: var(--paper);
    overflow: hidden;
    box-shadow: 0 6px 14px rgba(0,0,0,.18);
  }
  .banner__shape { position: absolute; inset: 0; width: 100%; height: 100%; }
  .logo-band {
    position: absolute;
    background: var(--brand-sky);
    display: flex; align-items: center; justify-content: center; gap: 8px;
    box-shadow: 0 2px 4px rgba(0,0,0,.2);
  }
  .logo-band__dot {
    width: 22px; height: 22px; border-radius: 50%;
    background: var(--paper);
  }
  .logo-band__name {
    font-family: "PT Sans", Arial, sans-serif;
    font-weight: 700; font-size: 29px; color: var(--paper);
    line-height: 1;
  }
  .photo {
    position: absolute;
    background: radial-gradient(ellipse at 45% 40%, var(--photo-light) 0%, var(--photo-mid) 55%, var(--photo-blue) 100%);
  }
  .headline {
    position: absolute;
    font-family: "PT Sans Narrow", "Arial Narrow", sans-serif;
    font-weight: 400;
    line-height: 1.0;
    text-align: center;
    letter-spacing: -0.5px;
  }
  .tagline {
    position: absolute;
    font-size: 16px; line-height: 1.25; text-align: center;
  }
  .cta {
    position: absolute;
    background: var(--cta-teal);
    font-family: "PT Sans Narrow", "Arial Narrow", sans-serif;
    font-weight: 700; font-size: 17px; letter-spacing: .3px;
    display: flex; align-items: center; justify-content: center;
    text-transform: uppercase;
  }

  /* Skyscraper 192 x 726 */
  .banner--sky { left: 310px; top: 160px; width: 192px; height: 726px; }
  .banner--sky .logo-band { left: 0; top: 0; width: 192px; height: 56px; }
  .banner--sky .photo { left: 0; top: 146px; width: 192px; height: 330px; }
  .banner--sky .headline { left: 0; width: 192px; top: 492px; font-size: 33px; }
  .banner--sky .tagline { left: 0; width: 192px; top: 594px; }
  .banner--sky .cta { left: 40px; top: 646px; width: 113px; height: 33px; }

  /* Square 364 x 301 */
  .banner--square { left: 614px; top: 584px; width: 364px; height: 301px; }
  .banner--square .photo { left: 0; top: 0; width: 200px; height: 301px; }
  .banner--square .logo-band { left: 160px; top: 0; width: 204px; height: 52px; }
  .banner--square .headline { left: 178px; width: 186px; top: 104px; font-size: 33px; }
  .banner--square .tagline { left: 178px; width: 186px; top: 196px; }
  .banner--square .cta { left: 216px; top: 244px; width: 113px; height: 33px; }

  /* Leaderboard 876 x 108 */
  .banner--wide { left: 161px; top: 970px; width: 876px; height: 108px; }
  .banner--wide .photo { left: 200px; top: 0; width: 240px; height: 108px; }
  .banner--wide .logo-band { left: 0; top: 0; width: 146px; height: 50px; }
  .banner--wide .headline { left: 480px; width: 200px; top: 20px; font-size: 33px; }
  .banner--wide .tagline { left: 690px; width: 166px; top: 12px; }
  .banner--wide .cta { left: 713px; top: 62px; width: 113px; height: 32px; }
</style>
</head>
<body>

  <section class="banner banner--sky" aria-label="Plume skyscraper banner">
    <div class="photo" role="img" aria-label="Photo of a smiling mother carrying her young son on her back"></div>
    <svg class="banner__shape" viewBox="0 0 192 726" preserveAspectRatio="none" aria-hidden="true">
      <path d="M0 380 Q70 395 192 458 L192 726 L0 726 Z" fill="var(--brand-deep)"/>
    </svg>
    <div class="logo-band"><span class="logo-band__dot"></span><span class="logo-band__name">plume</span></div>
    <h2 class="headline">Yourself,<br>Discovered.</h2>
    <p class="tagline">Everyone has a story.<br>Find yours.</p>
    <div class="cta">Sign up</div>
  </section>

  <section class="banner banner--square" aria-label="Plume square banner">
    <div class="photo" role="img" aria-label="Photo of a smiling mother carrying her young son on her back"></div>
    <svg class="banner__shape" viewBox="0 0 364 301" preserveAspectRatio="none" aria-hidden="true">
      <path d="M160 0 Q190 150 184 301 L364 301 L364 0 Z" fill="var(--brand-deep)"/>
    </svg>
    <div class="logo-band"><span class="logo-band__dot"></span><span class="logo-band__name">plume</span></div>
    <h2 class="headline">Yourself,<br>Discovered.</h2>
    <p class="tagline">Everyone has a story.<br>Find yours.</p>
    <div class="cta">Sign up</div>
  </section>

  <section class="banner banner--wide" aria-label="Plume leaderboard banner">
    <div class="photo" role="img" aria-label="Photo of a smiling mother with her young son hugging her"></div>
    <svg class="banner__shape" viewBox="0 0 876 108" preserveAspectRatio="none" aria-hidden="true">
      <path d="M419 0 Q460 50 487 108 L876 108 L876 0 Z" fill="var(--brand-deep)"/>
    </svg>
    <div class="logo-band"><span class="logo-band__dot"></span><span class="logo-band__name">plume</span></div>
    <h2 class="headline">Yourself,<br>Discovered.</h2>
    <p class="tagline">Everyone has a story.<br>Find yours.</p>
    <div class="cta">Sign up</div>
  </section>

</body>
</html>
```